Velmora Grid - Stock Certificate

We need a custom designed stock certificate that represents the look of our company logo but also have a cool look compared to a standard stock certificate. We thinking we want the logo in gold. Our website is https://www.velmoragridusa.example.

We are wanting the certificate to look very professional and really cool, we have sales agents that work for the company and we are creating a program by which the sales agents can gain ownership in the company. So the certificates need to have a very cool appeal and that provides a sense of pride in owning "Units" in Velmora Grid.
Updates

Project Deadline Extended
Reason: Extending so other board members can vote as well, thank you all!

Target Market(s)

Stock/Shareholders

Industry/Entity Type

It Company

Font styles to use
Script

Requirements
Must have
• Must look like a stock certificate, must use our logo which the psd file for it was attached.
Nice to have
• Nice to have the logo in gold

```html
<!DOCTYPE html>
<html lang="en">
<head>
<meta charset="utf-8">
<title>Velmora Grid – Stock Certificate</title>
<link rel="stylesheet" href="https://fonts.googleapis.com/css2?family=Dancing+Script:wght@600&family=Montserrat:wght@500&display=swap">
<style>
:root{
  --paper-light:#fffdd0;
  --paper-mid:#fbf3a6;
  --paper-warm:#f4e08e;
  --ink:#3b3a2c;
  --rule:#8a8570;
  --yellow:#fbd22c;
  --amber:#f7a414;
  --orange:#f5820d;
  --dark:#2a2414;
  --gold-light:#f9d86a;
  --gold:#e0a928;
  --gold-deep:#b47812;
}
*{margin:0;padding:0;box-sizing:border-box}
html,body{width:1200px;height:917px;overflow:hidden;background:#ffffff}
.certificate{
  position:relative;width:1200px;height:917px;overflow:hidden;
  background:linear-gradient(20deg,var(--paper-warm) 0%,var(--paper-mid) 35%,var(--paper-light) 70%);
  font-family:"Montserrat",sans-serif;color:var(--ink);
}
.decor{position:absolute;inset:0;width:100%;height:100%}
.title{
  position:absolute;left:96px;top:110px;
  font-family:"Dancing Script",cursive;font-weight:600;font-size:104px;line-height:1;
  color:var(--ink);letter-spacing:1px;
}
.caps{
  position:absolute;font-size:27px;font-variant:small-caps;letter-spacing:1px;
  white-space:nowrap;line-height:1;
}
.certify{left:250px;top:272px;font-size:26px}
.name-rule{position:absolute;left:34px;top:392px;width:760px;height:1px;background:var(--rule)}
.blank{position:absolute;height:1px;background:var(--ink)}
.seal{
  position:absolute;left:853px;top:172px;width:276px;height:276px;border-radius:50%;
  background:radial-gradient(circle at 40% 35%,var(--gold-light) 0%,var(--gold) 55%,var(--gold-deep) 100%);
  box-shadow:0 0 0 6px #f2c64a,0 6px 14px rgba(120,70,0,.35);
  display:flex;align-items:center;justify-content:center;
}
.seal-ring{position:absolute;inset:16px;border-radius:50%;border:2px solid var(--gold-light)}
.seal-name{
  position:relative;font-family:"Montserrat",sans-serif;font-weight:500;font-size:26px;
  color:#6a1e0c;letter-spacing:1px;text-align:center;line-height:1.15;
}
</style>
</head>
<body>
<main class="certificate">
  <svg class="decor" viewBox="0 0 1200 917" role="img" aria-label="Decorative diagonal colour bands in yellow, orange and black">
    <defs>
      <linearGradient id="cornerTone" x1="0" y1="0" x2="1" y2="1">
        <stop offset="0" stop-color="var(--amber)"/>
        <stop offset="1" stop-color="var(--yellow)"/>
      </linearGradient>
      <linearGradient id="bandTone" x1="0" y1="0" x2="1" y2="1">
        <stop offset="0" stop-color="var(--yellow)"/>
        <stop offset=".45" stop-color="var(--orange)"/>
        <stop offset=".8" stop-color="var(--dark)"/>
        <stop offset="1" stop-color="var(--amber)"/>
      </linearGradient>
    </defs>
    <polygon points="0,0 210,0 0,225" fill="url(#cornerTone)"/>
    <polygon points="1090,0 1200,0 1200,917 560,917 640,710" fill="url(#bandTone)"/>
  </svg>

  <h1 class="title">Stock Certificate</h1>
  <p class="caps certify">This is to certify that</p>
  <div class="name-rule"></div>

  <p class="caps" style="left:95px;top:458px">Is the OWNER of</p>
  <div class="blank" style="left:372px;top:482px;width:96px"></div>
  <p class="caps" style="left:491px;top:458px">shares of stock</p>

  <div class="blank" style="left:89px;top:564px;width:64px"></div>
  <p class="caps" style="left:169px;top:540px">On this</p>
  <div class="blank" style="left:296px;top:564px;width:80px"></div>
  <p class="caps" style="left:385px;top:540px">Day of</p>
  <div class="blank" style="left:491px;top:564px;width:81px"></div>
  <p class="caps" style="left:589px;top:540px">In the year</p>

  <div class="blank" style="left:41px;top:705px;width:114px"></div>
  <p class="caps" style="left:172px;top:681px">Signed</p>
  <div class="blank" style="left:41px;top:820px;width:114px"></div>
  <p class="caps" style="left:172px;top:796px">Signed</p>

  <div class="seal">
    <div class="seal-ring"></div>
    <span class="seal-name">Velmora<br>Grid</span>
  </div>
</main>
</body>
</html>
```